Vorel constructions

We are predominantly a residential home builder based in Melbourne, Victoria Australia. We construct houses, apartments, townhouses, multi-unit developments.

The name of the company is "Vorel Constructions"
My company believes in building unique construction projects mainly residential homes. The target customers are upmarket Melbourne residents/investors.

I want the brand name "Vorel" to be part of the logo. There's no need to put the word construction in the logo at this stage.

I would also like some ideas for a slogan e.g. "Just build it." or "We build quality homes." But I would like something unique and different for a slogan not the same old cliche.

vorelconstructions.example.com.au
e: tmelo@vorelconstructions.example.com.au
M: 0417305862
Address: 8/3 Fenwick Lane Clayton VIC 3168

Director:Mr Dinesh Malarkodiyan

```html
<!DOCTYPE html>
<html lang="en">
<head>
<meta charset="utf-8">
<title>Vorel Constructions – Business Card</title>
<link rel="stylesheet" href="https://fonts.googleapis.com/css2?family=Encode+Sans+Condensed:wght@400;500&display=swap">
<style>
  :root {
    --navy: #13295a;
    --cyan: #2bb8e8;
    --paper-light: #fafafa;
    --paper-mid: #e6e6e7;
    --paper-edge: #c9c9cb;
    --card-w: 1200px;
    --card-h: 757px;
  }
  html, body {
    margin: 0;
    padding: 0;
    width: var(--card-w);
    height: var(--card-h);
    overflow: hidden;
    background: #ffffff;
  }
  .card {
    position: relative;
    width: var(--card-w);
    height: var(--card-h);
    overflow: hidden;
    background: radial-gradient(ellipse 75% 80% at 40% 35%, var(--paper-light) 0%, var(--paper-mid) 60%, var(--paper-edge) 100%);
    font-family: "Encode Sans Condensed", "Arial Narrow", sans-serif;
    color: var(--navy);
  }
  .brand-name {
    position: absolute;
    left: 100px;
    top: 52px;
    margin: 0;
    font-size: 96px;
    font-weight: 500;
    line-height: 1;
    letter-spacing: 1px;
    color: var(--cyan);
  }
  .person {
    position: absolute;
    right: 84px;
    top: 58px;
    text-align: right;
  }
  .person-name {
    margin: 0;
    font-size: 45px;
    font-weight: 400;
    line-height: 1.1;
  }
  .person-role {
    margin: 0;
    font-size: 36px;
    font-weight: 400;
    line-height: 1.15;
  }
  .contact-list {
    position: absolute;
    left: 94px;
    top: 262px;
    margin: 0;
    padding: 0;
    list-style: none;
  }
  .contact-item {
    display: flex;
    align-items: center;
    height: 61px;
    font-size: 40px;
    line-height: 1;
  }
  .contact-icon {
    width: 44px;
    height: 34px;
    margin-right: 35px;
    fill: var(--navy);
    flex: none;
  }
  .contact-item.is-mobile .contact-text { margin-left: 6px; }
  .swoosh {
    position: absolute;
    left: 0;
    bottom: 0;
    width: var(--card-w);
    height: var(--card-h);
  }
  .slogan {
    position: absolute;
    right: 84px;
    bottom: 26px;
    margin: 0;
    font-size: 31px;
    font-style: italic;
    font-weight: 400;
    color: var(--cyan);
  }
</style>
</head>
<body>
<main class="card">
  <p class="brand-name">Vorel</p>

  <header class="person">
    <h1 class="person-name">Dinesh Malarkodiyan</h1>
    <p class="person-role">Director</p>
  </header>

  <ul class="contact-list">
    <li class="contact-item is-phone">
      <svg class="contact-icon" viewBox="0 0 44 34" aria-hidden="true">
        <path d="M12 3 L17 9 C18 10.5 17.5 12 16 13 L14 14.5 C16 19 19.5 22.5 24 24.5 L25.5 22.5 C26.5 21 28 20.5 29.5 21.5 L35 26 C36 27 36 28.5 35 29.5 L32 32 C30 33.5 27 33.5 24 32 C15 28 8 20 5 11 C4 8 4.5 6 6 4.5 L9 2.5 C10 1.8 11.2 2 12 3 Z"/>
      </svg>
      <span class="contact-text">03 9481 6630</span>
    </li>
    <li class="contact-item is-fax">
      <svg class="contact-icon" viewBox="0 0 44 34" aria-hidden="true">
        <rect x="11" y="2" width="22" height="9" rx="1"/>
        <path d="M4 12 H40 C42 12 43 13 43 15 V26 H36 V21 H8 V26 H1 V15 C1 13 2 12 4 12 Z"/>
        <rect x="10" y="23" width="24" height="10" rx="1"/>
      </svg>
      <span class="contact-text">03 9481 6631</span>
    </li>
    <li class="contact-item is-mobile">
      <svg class="contact-icon" viewBox="0 0 44 34" aria-hidden="true">
        <path d="M13 4 H31 C32.5 4 33 5 33 6 V32 C33 33 32.5 34 31 34 H13 C11.5 34 11 33 11 32 V6 C11 5 11.5 4 13 4 Z M14 7 V15 H30 V7 Z"/>
        <rect x="14" y="0" width="3" height="5"/>
        <g fill="#e6e6e7">
          <rect x="15" y="18" width="3" height="3"/><rect x="20.5" y="18" width="3" height="3"/><rect x="26" y="18" width="3" height="3"/>
          <rect x="15" y="23" width="3" height="3"/><rect x="20.5" y="23" width="3" height="3"/><rect x="26" y="23" width="3" height="3"/>
          <rect x="15" y="28" width="3" height="3"/><rect x="20.5" y="28" width="3" height="3"/><rect x="26" y="28" width="3" height="3"/>
        </g>
      </svg>
      <span class="contact-text">0417305862</span>
    </li>
    <li class="contact-item is-email">
      <svg class="contact-icon" viewBox="0 0 44 34" aria-hidden="true">
        <path d="M2 7 H42 L22 20 Z"/>
        <path d="M2 10 L15 18.5 L2 28 Z"/>
        <path d="M42 10 L29 18.5 L42 28 Z"/>
        <path d="M17.5 20 L22 23 L26.5 20 L42 30 H2 Z"/>
      </svg>
      <span class="contact-text">tmelo@vorelconstructions.example.com.au</span>
    </li>
    <li class="contact-item is-web">
      <svg class="contact-icon" viewBox="0 0 44 34" aria-hidden="true">
        <circle cx="22" cy="17" r="16"/>
        <g fill="none" stroke="#e6e6e7" stroke-width="1.8">
          <ellipse cx="22" cy="17" rx="7" ry="15"/>
          <line x1="6" y1="17" x2="38" y2="17"/>
          <path d="M9 9 H35 M9 25 H35"/>
        </g>
      </svg>
      <span class="contact-text">vorelconstructions.example.com.au</span>
    </li>
  </ul>

  <svg class="swoosh" viewBox="0 0 1200 757" aria-hidden="true">
    <path d="M288 757 C 500 662, 790 592, 1200 612 L1200 757 Z" fill="var(--cyan)"/>
    <path d="M330 757 C 560 672, 850 622, 1200 630 L1200 757 Z" fill="var(--navy)"/>
  </svg>

  <p class="slogan">Homes shaped around how you live.</p>
</main>
</body>
</html>
```